Veda K Art Studio Business Card Layout

Hi, I have a logo but I need help laying it out on a business card. I would like to include the following:
The Logo (see attached)
vedakartstudio.com
veda@vedakartstudio.com

Industry/Entity Type

Business

```html
<!DOCTYPE html>
<html lang="en">
<head>
<meta charset="utf-8">
<title>Veda K Art Studio – Business Card</title>
<link rel="stylesheet" href="https://fonts.googleapis.com/css2?family=Montserrat:wght@500;600&display=swap">
<style>
  :root {
    --backdrop: #e9e6e1;
    --card-white: #ffffff;
    --gold-light: #cdbd85;
    --gold-mid: #b4a16a;
    --gold-dark: #998455;
    --gold-icon: #a89256;
    --ink-white: #ffffff;
    --ink-grey: #6e675a;
  }
  * { box-sizing: border-box; margin: 0; padding: 0; }
  html, body {
    width: 1200px;
    height: 800px;
    overflow: hidden;
    background: var(--backdrop);
    font-family: "Montserrat", sans-serif;
  }
  .business-card {
    position: absolute;
    left: 75px;
    top: 100px;
    width: 1050px;
    height: 600px;
    background: var(--card-white);
    border-radius: 26px;
    overflow: hidden;
    box-shadow: 0 10px 30px rgba(60, 50, 30, 0.18);
  }
  .gold-band {
    position: absolute;
    left: 0;
    top: 0;
    width: 100%;
    height: 252px;
    background: linear-gradient(100deg, var(--gold-light) 0%, var(--gold-mid) 55%, var(--gold-dark) 100%);
  }
  .logo-disc {
    position: absolute;
    left: 72px;
    top: 86px;
    width: 380px;
    height: 380px;
    border-radius: 50%;
    background: var(--card-white);
    display: flex;
    align-items: center;
    justify-content: center;
  }
  .studio-name {
    color: var(--ink-grey);
    font-weight: 500;
    font-size: 29px;
    line-height: 1;
    white-space: nowrap;
  }
  .holder {
    position: absolute;
    left: 546px;
    top: 178px;
    color: var(--ink-white);
  }
  .holder-name {
    font-weight: 600;
    font-size: 38px;
    line-height: 1;
  }
  .holder-role {
    font-weight: 500;
    font-size: 23px;
    margin-top: 4px;
  }
  .contact-list {
    position: absolute;
    left: 546px;
    top: 330px;
    list-style: none;
  }
  .contact-item {
    display: flex;
    align-items: center;
    gap: 20px;
    height: 46px;
    color: var(--ink-grey);
    font-weight: 500;
    font-size: 29px;
  }
  .contact-icon {
    width: 24px;
    height: 24px;
    flex: none;
    fill: none;
    stroke: var(--gold-icon);
    stroke-width: 2.4;
    stroke-linecap: round;
    stroke-linejoin: round;
  }
</style>
</head>
<body>
  <main class="business-card">
    <div class="gold-band"></div>

    <div class="logo-disc" role="img" aria-label="Studio logo area">
      <p class="studio-name">Veda K Art Studio</p>
    </div>

    <div class="holder">
      <p class="holder-name">Sam Rivers</p>
      <p class="holder-role">Director</p>
    </div>

    <ul class="contact-list">
      <li class="contact-item">
        <svg class="contact-icon" viewBox="0 0 24 24" aria-hidden="true">
          <rect x="6" y="2" width="12" height="20" rx="2"/>
          <line x1="10" y1="18" x2="14" y2="18"/>
        </svg>
        <span>61455019283</span>
      </li>
      <li class="contact-item">
        <svg class="contact-icon" viewBox="0 0 24 24" aria-hidden="true">
          <circle cx="12" cy="12" r="10"/>
          <ellipse cx="12" cy="12" rx="4" ry="10"/>
          <line x1="2" y1="12" x2="22" y2="12"/>
        </svg>
        <span>vedakartstudio.com</span>
      </li>
      <li class="contact-item">
        <svg class="contact-icon" viewBox="0 0 24 24" aria-hidden="true">
          <circle cx="12" cy="12" r="4"/>
          <path d="M16 8v5a3 3 0 0 0 6 0v-1a10 10 0 1 0-4 8"/>
        </svg>
        <span>veda@vedakartstudio.com</span>
      </li>
    </ul>
  </main>
</body>
</html>
```